Menu Design Project

Menu design for a Japanese fast food restaurant featuring Teppanyaki and Sushi. The restaurant main scene color is black and wood color. No Japan scenery pictures. Menu try to be simply and elegant . Pictures provided can be used accordingly to the menu items, but doesn't have to be due to the back ground color of the picture is white.

Target Market(s)

Young and progressive consumers

Industry/Entity Type

Asian Restaurant

Other font styles liked:
• Han Wang Kan Tan Font

Colors
1b1b1b
fee18a

Requirements
Must have
• Pictures of the Sushi that is provided, and all the item in the Word file.
Nice to have
• Keep it simple but different
Should not have
• No scenery pictures, no cherry blossom.

```html
<!DOCTYPE html>
<html lang="en">
<head>
<meta charset="utf-8">
<title>Teppan House Menu</title>
<link href="https://fonts.googleapis.com/css2?family=Lilita+One&family=Lato:ital,wght@0,400;0,700;0,900;1,400&display=swap" rel="stylesheet">
<style>
:root{
  --ink:#1b1b1b;
  --cream:#fee18a;
  --wood-light:#ecd6a2;
  --wood-mid:#e0c085;
  --wood-dark:#d2ac6c;
  --panel:#f6e3ae;
  --photo-warm:#e9c9a4;
  --photo-pale:#f1e6d6;
  --text:#2a2218;
}
*{margin:0;padding:0;box-sizing:border-box}
html,body{width:756px;height:1200px;overflow:hidden;background:var(--cream)}
body{position:relative;font-family:"Lato",sans-serif;color:var(--text)}
.page{position:absolute;left:0;width:756px;overflow:hidden}
.page--front{top:0;height:588px}
.page--inside{top:612px;height:588px}
.page-bands{position:absolute;inset:0}
.abs{position:absolute}
.section-title{font-family:"Lilita One",sans-serif;color:var(--cream);font-size:28px;letter-spacing:.5px;text-shadow:0 0 3px var(--ink),1px 1px 0 var(--ink)}
.section-band{position:absolute;background:var(--ink);border-radius:2px;transform:skewX(-12deg)}
.sub-title{font-weight:900;font-size:10px;text-decoration:underline;color:var(--ink)}
.row{display:flex;justify-content:space-between;font-size:7.6px;line-height:9.6px}
.item-name{font-weight:700;font-size:7.6px;line-height:9.5px;color:var(--ink)}
.item-desc{font-style:italic;font-size:6.3px;line-height:8px}
.block{font-size:7px;line-height:9.2px}
.block b{color:var(--ink)}
.small{font-size:6.3px;line-height:8.6px}
.photo{position:absolute;border:1.5px solid var(--ink);background:linear-gradient(135deg,var(--photo-warm),var(--photo-pale))}
.thumb{position:absolute;background:linear-gradient(135deg,#ffffff,var(--photo-pale));border:1px solid #c9b48a;clip-path:polygon(0 0,86% 0,100% 50%,86% 100%,0 100%)}
.thumb--flip{clip-path:polygon(14% 0,100% 0,100% 100%,14% 100%,0 50%)}
.roll{position:absolute}
.center{text-align:center}
</style>
</head>
<body>

<!-- Front page -->
<section class="page page--front">
  <svg class="page-bands" width="756" height="588" viewBox="0 0 756 588">
    <defs>
      <linearGradient id="woodFront" x1="0" y1="0" x2="1" y2="1">
        <stop offset="0" stop-color="#ead29c"/>
        <stop offset=".5" stop-color="#e2c58c"/>
        <stop offset="1" stop-color="#d8b475"/>
      </linearGradient>
    </defs>
    <rect width="756" height="588" fill="var(--cream)"/>
    <path d="M0 30 Q380 18 756 22 L756 555 Q380 548 0 562 Z" fill="url(#woodFront)"/>
    <rect x="264" y="28" width="228" height="526" fill="var(--panel)" opacity=".7"/>
    <path d="M0 22 Q380 10 756 16 L756 24 Q380 20 0 36 Z" fill="var(--ink)"/>
    <path d="M0 556 Q380 544 756 552 L756 562 Q380 552 0 566 Z" fill="var(--ink)"/>
  </svg>

  <div class="section-band" style="left:64px;top:30px;width:130px;height:20px"></div>
  <h1 class="section-title abs" style="left:72px;top:18px">Appetizer</h1>

  <div class="abs" style="left:20px;top:70px;width:214px">
    <div class="row"><span class="item-name">Seaweed Salad</span></div>
    <div class="row"><span class="item-desc">seasoned seaweed</span><span>2.99</span></div>
    <div class="row"><span class="item-name">Kani Salad <i>Spicy or Non-Spicy</i></span></div>
    <div class="row"><span class="item-desc">crab meat, cucumber, lettuce with dressing</span><span>3.99</span></div>
    <div class="row"><span class="item-name">Tempura Shrimp</span></div>
    <div class="row"><span class="item-desc">4 Pieces Fried Tempura Shrimp</span><span>5.99</span></div>
    <div class="row"><span class="item-name">Fried Gyoza (6pcs)</span><span>3.99</span></div>
    <div class="row"><span class="item-name">Spring Roll (4pcs)</span><span>2.59</span></div>
    <div class="row"><span class="item-name">Crab Rangoon (5pcs)</span><span>4.50</span></div>
  </div>

  <div class="abs block" style="left:16px;top:170px;width:220px">
    <b>Sashimi</b><br><i class="small">*Salmon, *Tuna, *Yellow Tail, *Red Snapper, *White Tuna, Surf Clam</i>
  </div>
  <div class="abs block" style="left:16px;top:210px;width:220px">
    <b>Sushi Nigiri 5 pieces for $5.99</b><br><i class="small">*Salmon, *Tuna, *Yellow Tail, *Red Snapper, *White Tuna, Surf Clam, Grill Eel, Ebi Shrimp, Kani crab meat</i>
  </div>
  <div class="abs block" style="left:16px;top:262px;width:222px">
    <b>Hand Roll Build your own: 2 for $5.99</b><br>
    <span class="small"><b>Pick one protein:</b> <i>*Salmon, *Tuna, *Yellow Tail, *Red Snapper, *White Tuna, Surf Clam, Grill Eel, Ebi Shrimp, Kani crab meat</i><br>
    <b>Pick two Vegetable:</b> <i>Cucumber, Avocado, Lettuce, Oshigo, Asparagus, Seaweed</i><br>
    <b>Pick Sauce:</b> <i>Spicy Mayonnaise, Honey Wasabi, Honey Mayonnaise, Unagi Sauce</i></span>
  </div>

  <div class="abs sub-title" style="left:16px;top:351px">Beverage</div>
  <div class="abs block" style="left:16px;top:372px;width:230px">
    <b>Fountain $1.79</b> <i class="small">(one free refill): Cola, Diet Cola, Cherry Soda, Lemon-Lime Soda, Orange Soda, Fruit Punch</i><br>
    <i class="small">Fresh Brew Ice Tea</i><br>
    <b>Bottle Drinks $1.49</b> <i class="small">Teas, Juices, Sports Drinks</i>
  </div>

  <div class="abs sub-title" style="left:16px;top:422px">Sides</div>
  <div class="abs" style="left:16px;top:444px;width:214px">
    <div class="row"><span>Fried Rice</span><span>2.59</span></div>
    <div class="row"><span>Yakisoba Noodle</span><span>3.59</span></div>
    <div class="row"><span>Mix Vegetable</span><span>3.59</span></div>
    <div class="row"><span>Yakisoba Noodle &amp; Vegetable</span><span>5.59</span></div>
    <div class="row"><span>Yakisoba Noodle &amp; Rice</span><span>5.59</span></div>
    <div class="row"><span>YumYum Sauce</span><span>0.50</span></div>
  </div>
  <p class="abs small" style="left:16px;top:515px;width:224px;font-weight:700;color:var(--ink)">*Items may be served raw or under cooked consuming raw or undercooked meat, poultry, shellfish, eggs or seafood may increase your risk of food borne illness.</p>

  <div class="abs center block" style="left:272px;top:60px;width:212px">
    <b>Food Allergy Advisory:</b><br>
    For your personal well-being, &amp; due to our broad range of food ingredients choices, if you have any food allergy, we strongly recommend you do not order food from Teppan House. Teppan House uses following ingredients but NOT limit to those may or may not CONTAINS and/or TRACE of those ingredients: Peanut, Soy, Dairy, Shellfish, Wheat, Egg, Gluten, etc.<br>
    Please inform the cashier any type of good allergy you may have before you place your order. Thank you for your understanding.
  </div>

  <div class="photo" role="img" aria-label="Photo of packaged sushi trays on display" style="left:266px;top:203px;width:222px;height:214px;background:linear-gradient(135deg,#3a2b22,#c7694a 35%,#e8d6bc 60%,#2a2622)"></div>

  <div class="abs center block" style="left:290px;top:484px;width:176px;font-weight:900;color:var(--ink);font-size:7.6px;line-height:10px">
    Teppan House<br>540-555-0142<br>Maple Ridge Mall/Food Court<br>1250 Maple Ridge Blvd. Unit 160<br>Riverton VA 24000
  </div>

  <div class="abs" role="img" aria-label="Large brushed Japanese character for grill" style="left:566px;top:84px;width:132px;height:118px;background:radial-gradient(ellipse at center,#3a3a3a,#1b1b1b 70%,transparent 72%)"></div>
  <div class="abs" role="img" aria-label="Close-up photo of a sushi roll with salmon, avocado and orange roe" style="left:544px;top:268px;width:212px;height:290px;border-radius:48% 0 0 40%;background:linear-gradient(160deg,#e77a2f 0%,#f2d9c0 30%,#f4b08e 45%,#e8df7a 65%,#f7f2e6 85%)"></div>
</section>

<!-- Inside page -->
<section class="page page--inside">
  <svg class="page-bands" width="756" height="588" viewBox="0 0 756 588">
    <defs>
      <linearGradient id="woodInside" x1="0" y1="0" x2="1" y2="1">
        <stop offset="0" stop-color="#ead29c"/>
        <stop offset=".5" stop-color="#e2c58c"/>
        <stop offset="1" stop-color="#d8b475"/>
      </linearGradient>
    </defs>
    <rect width="756" height="588" fill="var(--cream)"/>
    <path d="M0 30 Q380 20 756 14 L756 560 Q380 566 0 572 Z" fill="url(#woodInside)"/>
    <path d="M0 24 Q380 16 756 8 L756 18 Q380 22 0 38 Z" fill="var(--ink)"/>
    <path d="M0 566 Q380 558 756 552 L756 562 Q380 566 0 578 Z" fill="var(--ink)"/>
  </svg>

  <div class="section-band" style="left:84px;top:46px;width:110px;height:18px"></div>
  <h2 class="section-title abs" style="left:92px;top:30px">Entree</h2>
  <p class="abs center" style="left:40px;top:60px;width:190px;font-style:italic;font-size:8.4px;line-height:10px">with Hibachi Vegetable and Fried Rice, or Yakisoba Noodle add 0.99</p>

  <div class="abs" style="left:22px;top:82px;width:214px">
    <div class="row"><span>Teriyaki Chicken</span><span>6.89</span></div>
    <div class="row"><span>(double Chicken Special 1.59)</span><span></span></div>
    <div class="row"><span>Teriyaki Beef</span><span>7.29</span></div>
    <div class="row"><span>Teriyaki Shrimp</span><span>7.89</span></div>
    <div class="row"><span>Teriyaki Chicken &amp; Shrimp</span><span>8.89</span></div>
    <div class="row"><span>Teriyaki Chicken &amp; Beef</span><span>8.49</span></div>
    <div class="row"><span>Teriyaki Beef &amp; Shrimp</span><span>9.29</span></div>
    <div class="row"><span>Teriyaki Chicken Beef &amp; Shrimp</span><span>10.29</span></div>
    <div class="row"><span>Hibachi Chicken</span><span>7.59</span></div>
    <div class="row"><span>Hibachi Beef</span><span>7.99</span></div>
    <div class="row"><span>Hibachi Shrimp</span><span>8.59</span></div>
    <div class="row"><span>Hibachi Chicken &amp; Shrimp</span><span>9.59</span></div>
    <div class="row"><span>Hibachi Chicken &amp; Beef</span><span>9.19</span></div>
    <div class="row"><span>Hibachi Beef &amp; Shrimp</span><span>9.99</span></div>
    <div class="row"><span>Hibachi Chicken, Beef &amp; Shrimp</span><span>10.99</span></div>
  </div>

  <div class="section-band" style="left:36px;top:254px;width:180px;height:14px"></div>
  <h2 class="section-title abs" style="left:98px;top:248px">Sushi</h2>
  <p class="abs" style="left:72px;top:282px;font-style:italic;font-size:8.4px">Ingredients subject to availability</p>
  <div class="abs sub-title" style="left:30px;top:303px">Special Roll</div>

  <!-- Left column rolls -->
  <div class="thumb thumb--flip" role="img" aria-label="Dragon roll photo" style="left:164px;top:310px;width:74px;height:54px"></div>
  <div class="roll" style="left:24px;top:336px;width:150px"><div class="item-name">Dragon Roll</div><div class="item-desc">Grilled Eel fish &amp; cucumber top with avocado &amp; Unagi sauce 9.99</div></div>
  <div class="roll" style="left:24px;top:378px;width:200px"><div class="item-name">Deluxe Black Dragon Roll</div><div class="item-desc">Tempura Shrimp top with Avocado, Grilled Eel fish &amp; Unagi sacue 11.99</div></div>
  <div class="thumb" role="img" aria-label="Rainbow roll photo" style="left:26px;top:414px;width:70px;height:54px"></div>
  <div class="roll" style="left:106px;top:428px;width:150px"><div class="item-name">*Rainbow Roll</div><div class="item-desc">avocado, cucumber &amp; Kani top with red snapper, tuna, salmon&amp;avocado 10.99</div></div>
  <div class="thumb thumb--flip" role="img" aria-label="Four season roll photo" style="left:164px;top:472px;width:74px;height:54px"></div>
  <div class="roll" style="left:24px;top:488px;width:140px"><div class="item-name">*Four Season Roll</div><div class="item-desc">Tuna, salmon, oshinko 9.99</div></div>
  <div class="roll" style="left:24px;top:530px;width:190px"><div class="item-name">*Deluxe Philly Roll</div><div class="item-desc">Salmon, cream cheese &amp; avocado top with more salmon 9.99</div></div>

  <!-- Middle column rolls -->
  <div class="thumb" role="img" aria-label="Massago roll photo" style="left:266px;top:32px;width:70px;height:46px"></div>
  <div class="roll" style="left:350px;top:44px;width:130px"><div class="item-name">*Massago Roll</div><div class="item-desc">Kani crab meat, cucumber &amp; avocado top with Premium Massago Roe 8.99</div></div>
  <div class="roll" style="left:266px;top:94px;width:148px"><div class="item-name">*Deluxe Spicy Tuna Roll</div><div class="item-desc">Kani crab meat, Cucumber &amp; avocado top with Spicy grounded tuna 9.49</div></div>
  <div class="thumb thumb--flip" role="img" aria-label="Deluxe spicy tuna roll photo" style="left:416px;top:84px;width:70px;height:56px"></div>
  <div class="thumb" role="img" aria-label="Deluxe spicy kani roll photo" style="left:266px;top:144px;width:70px;height:56px"></div>
  <div class="roll" style="left:352px;top:156px;width:130px"><div class="item-name">Deluxe Spicy Kani Roll</div><div class="item-desc">Kani crab meat, cucumber &amp; avocado top with seasoned ground Crab meat 9.49</div></div>
  <div class="roll" style="left:266px;top:216px;width:148px"><div class="item-name">Deluxe Kani Roll</div><div class="item-desc">Kani crab meat, cucumber &amp; avocado top with Kani &amp; Panko crumb 9.49</div></div>
  <div class="thumb thumb--flip" role="img" aria-label="Deluxe kani roll photo" style="left:416px;top:204px;width:70px;height:56px"></div>
  <div class="thumb" role="img" aria-label="Tri deluxe fish roll photo" style="left:266px;top:264px;width:70px;height:54px"></div>
  <div class="roll" style="left:352px;top:276px;width:130px"><div class="item-name">*Tri Deluxe Fish Roll</div><div class="item-desc">Tuna, salmon &amp; red snapper 9.99</div></div>
  <div class="roll" style="left:266px;top:346px;width:220px"><div class="item-name">*Sumo Roll Tuna</div><div class="item-desc">Salmon, White Tuan, Red snapper Avocado &amp; Kani Crab Meat 10.99</div></div>
  <div class="roll" style="left:266px;top:396px;width:220px"><div class="item-name">*Hamachi Asparagus Roll</div><div class="item-desc">Hamachi, Scallion &amp; Asparagus with Ponzu Sauce 7.99</div></div>
  <div class="abs sub-title" style="left:272px;top:420px">Regular Maki Roll</div>
  <div class="roll" style="left:266px;top:458px;width:150px"><div class="item-name">*Salmon Roll</div><div class="item-desc">salmon &amp; avocado (8pcs) 5.49 (12pcs) 7.49</div></div>
  <div class="thumb thumb--flip" role="img" aria-label="Salmon roll photo" style="left:420px;top:446px;width:66px;height:54px"></div>
  <div class="thumb" role="img" aria-label="Tuna roll photo" style="left:266px;top:496px;width:66px;height:54px"></div>
  <div class="roll" style="left:352px;top:518px;width:134px"><div class="item-name">*Tuna Roll</div><div class="item-desc">tuna &amp; avocado (8pcs) 5.49 (12pcs) 7.49</div></div>

  <!-- Right column rolls -->
  <div class="roll" style="left:514px;top:36px;width:220px"><div class="item-name">*Philly Roll</div><div class="item-desc">salmon, cream cheese &amp; avocado (8pcs) 5.49 (12pcs) 7.49</div></div>
  <div class="roll" style="left:514px;top:86px;width:220px"><div class="item-name">California Roll</div><div class="item-desc">cucumber, avocado &amp; kani crab meat (8pcs) 5.49 (12pcs) 7.49</div></div>
  <div class="roll" style="left:514px;top:136px;width:220px"><div class="item-name">Kani &amp; Cheese Roll</div><div class="item-desc">Kani crab meat &amp; cream cheese (8pcs) 5.49 (12pcs) 7.49</div></div>
  <div class="thumb" role="img" aria-label="Shrimp tempura roll photo" style="left:514px;top:170px;width:68px;height:54px"></div>
  <div class="roll" style="left:596px;top:188px;width:150px"><div class="item-name">Shrimp Tempura Roll</div><div class="item-desc">Fried tempura shrimp &amp; cucumber (8pcs) 6.49</div></div>
  <div class="roll" style="left:514px;top:248px;width:132px"><div class="item-name">*Alaska Roll</div><div class="item-desc">Salmon &amp; avocado with massago (8pcs) 5.49 (12pcs) 7.49</div></div>
  <div class="thumb thumb--flip" role="img" aria-label="Alaska roll photo" style="left:656px;top:232px;width:74px;height:56px"></div>
  <div class="thumb" role="img" aria-label="Grilled eel hand roll photo" style="left:514px;top:298px;width:68px;height:54px"></div>
  <div class="roll" style="left:596px;top:318px;width:140px"><div class="item-name">Grilled Eel Roll</div><div class="item-desc">Eel &amp; avocado (8pcs) 5.49 (12pcs) 7.49</div></div>
  <div class="roll" style="left:514px;top:368px;width:220px"><div class="item-name">*Spicy Tuna Roll</div><div class="item-desc">seasoned ground tuna (8pcs) 5.49 (12pcs) 7.49</div></div>
  <div class="roll" style="left:514px;top:420px;width:220px"><div class="item-name">*Spicy Salmon Roll</div><div class="item-desc">seasoned ground salmon (8pcs) 5.49 (12pcs) 7.49</div></div>
  <div class="roll" style="left:514px;top:458px;width:140px"><div class="item-name">Spicy Kani Roll</div><div class="item-desc">seasoned ground crab meat (8pcs) 5.49 (12pcs) 7.49</div></div>
  <div class="thumb thumb--flip" role="img" aria-label="Spicy kani roll photo" style="left:662px;top:448px;width:68px;height:54px"></div>
  <div class="roll" style="left:514px;top:510px;width:220px"><div class="item-name">Vegetarian Roll</div><div class="item-desc">avocado, cucumber (8pcs) 4.49 (16pcs) 7.99<br>Add Ajitsuke seasoned fried bean curd for $1.00 more</div></div>
</section>

</body>
</html>
```